Marlow Crest Group (Real Estate and Investment)

A high end, clean design.
We are a real estate company with sales, asset management and investment divisions. We want to use a black and white scheme which is really high end feel. The back of the card can just be the logo (black background with the white writing) as we will probably emboss this when we print)

Target Market(s)

High level investors, high end houses for sale

Industry/Entity Type

Business

Contact Information for Business Card

Name, position, phone number and email address
Glen Varley, Managing Director, 0437259064 and glen@marlowcrest-example.com.au

Requirements
Must have
• Back of the card to be the black background with the white writing (as per the attached images). Would like the capacity to emboss the writing and logo

```html
<!DOCTYPE html>
<html lang="en">
<head>
<meta charset="utf-8">
<title>Marlow Crest Group – Business Card</title>
<link rel="stylesheet" href="https://fonts.googleapis.com/css2?family=Montserrat:wght@400;500;700&family=Roboto:wght@400&display=swap">
<style>
  :root {
    --backdrop: #e6e4e1;
    --card-black: #141414;
    --emboss-grey: #2c2c2c;
    --paper: #fbfbfa;
    --ink: #111111;
    --rule: #8a8a8a;
    --band-text: #ffffff;
  }
  * { box-sizing: border-box; margin: 0; padding: 0; }
  html, body { width: 1200px; height: 716px; overflow: hidden; }
  body {
    background: var(--backdrop);
    position: relative;
    font-family: "Roboto", Arial, sans-serif;
  }
  .card {
    position: absolute;
    top: 208px;
    width: 540px;
    height: 300px;
    overflow: hidden;
  }

  /* Back of card */
  .card-back { left: 30px; background: var(--card-black); }
  .card-back .brand {
    position: absolute;
    left: 0; right: 0; top: 104px;
    display: flex; flex-direction: column; align-items: center; gap: 16px;
  }
  .brand-dot {
    width: 54px; height: 54px; border-radius: 50%;
    border: 2px solid var(--emboss-grey);
  }
  .card-back .brand-name {
    font-family: "Montserrat", Arial, sans-serif;
    font-weight: 500;
    font-size: 26px;
    letter-spacing: 0.5px;
    color: var(--emboss-grey);
    text-transform: uppercase;
  }

  /* Front of card */
  .card-front { left: 630px; background: var(--paper); color: var(--ink); }
  .holder { position: absolute; left: 26px; top: 112px; }
  .holder-name {
    font-family: "Montserrat", Arial, sans-serif;
    font-size: 21px; font-weight: 400; letter-spacing: 0.5px;
    text-transform: uppercase;
  }
  .holder-name strong { font-weight: 700; }
  .holder-role { font-size: 11px; margin-top: 2px; }
  .divider {
    position: absolute; left: 26px; right: 56px; top: 160px;
    height: 1px; background: var(--rule);
  }
  .contacts {
    position: absolute; left: 26px; top: 172px;
    list-style: none; font-size: 14px;
  }
  .contacts li { display: flex; align-items: center; gap: 10px; height: 22px; }
  .contacts svg { width: 14px; height: 14px; fill: var(--ink); flex: none; }
  .card-front .brand {
    position: absolute; right: 34px; top: 64px;
    display: flex; flex-direction: column; align-items: center; gap: 12px;
  }
  .card-front .brand-dot { border-color: var(--ink); width: 60px; height: 60px; }
  .card-front .brand-name {
    font-family: "Montserrat", Arial, sans-serif;
    font-weight: 500; font-size: 20px; letter-spacing: 0.3px;
    text-transform: uppercase; color: var(--ink);
  }
  .footer-band { position: absolute; left: 0; bottom: 0; width: 540px; height: 48px; }
  .web-address {
    position: absolute; right: 22px; bottom: 12px;
    font-size: 14px; color: var(--band-text); letter-spacing: 0.2px;
  }
</style>
</head>
<body>

<section class="card card-back" aria-label="Card back">
  <div class="brand">
    <span class="brand-dot"></span>
    <span class="brand-name">Marlow Crest Group</span>
  </div>
</section>

<section class="card card-front" aria-label="Card front">
  <div class="brand">
    <span class="brand-dot"></span>
    <span class="brand-name">Marlow Crest Group</span>
  </div>

  <div class="holder">
    <p class="holder-name">Glen <strong>Varley</strong></p>
    <p class="holder-role">Managing Director</p>
  </div>

  <div class="divider"></div>

  <ul class="contacts">
    <li>
      <svg viewBox="0 0 24 24" aria-hidden="true"><path d="M6.6 10.8a15.1 15.1 0 0 0 6.6 6.6l2.2-2.2c.3-.3.7-.4 1-.2 1.1.4 2.3.6 3.6.6.6 0 1 .4 1 1V20c0 .6-.4 1-1 1A17 17 0 0 1 3 4c0-.6.4-1 1-1h3.5c.6 0 1 .4 1 1 0 1.3.2 2.5.6 3.6.1.3 0 .7-.2 1z"/></svg>
      <span>0437259064</span>
    </li>
    <li>
      <svg viewBox="0 0 24 24" aria-hidden="true"><path d="M2 5h20v14H2zm2 2v.5l8 5 8-5V7zm0 2.8V17h16V9.8l-8 5z"/></svg>
      <span>glen@marlowcrest-example.com.au</span>
    </li>
  </ul>

  <svg class="footer-band" viewBox="0 0 540 48" aria-hidden="true">
    <polygon points="0,40 268,40 262,48 0,48" fill="#111111"/>
    <polygon points="278,30 282,30 266,48 262,48" fill="#111111"/>
    <polygon points="296,0 540,0 540,48 262,48" fill="#111111"/>
  </svg>
  <span class="web-address">www.marlowcrest-example.com.au</span>
</section>

</body>
</html>
```